依頼詳細
新規開院に併せて内覧会を開催いたします。
その告知用に折込チラシの配布・ポスティング配布を実施します。
地域の皆様に開院を広く知っていただけるようなシンプルかつインパクトのある、わかりやすいチラシデザインをお願いいたします。ベースのカラーはピンク系が希望です。
女性・高齢者の方に院を知っていただき、アピールできるようなデザインをお願いいたします。
記載項目
・院名/住所/電話番号/施術受付時間/地図/院長よりメッセージなど。
・内覧会開催のお知らせ、開催日(変更になる可能性があります)
・オープンに先がけて内覧会を開催します。
・実際のオープン日など(変更になる可能性があります)
サイズ
A4
ページ数
片面
希望イメージ
シンプル 複雑
単色 カラフル
暗い 明るい
日常 高級
遊び心 厳粛
未来的 伝統的
女性的 男性的
希望する色
赤系、ピンクを中心にお願いいたします。
納品ファイル
• 高解像度JPG (.jpg)
• イラストレーター形式 (.ai)
補足説明
新規開業の接骨院の為、地域の皆様に認知していただけるような親しみがあり、インパクトのあるチラシデザインをお願いいたします。

シンプルでわかりやすいイメージが気に入りました。
地域の皆様に愛される接骨院のイメージが沸きましたので、このデザインに決定いたしました。

たくさんのご提案ありがとうございました。
決定までお時間をいただき申し訳ありませんでしたが、
最初の直感で決定いたしました。またの機会がございましたら
ご提案宜しくお願いいたします。

```html
<!DOCTYPE html>
<html lang="ja">
<head>
<meta charset="utf-8">
<title>さくらだ接骨院 開院・内覧会のお知らせ</title>
<link rel="stylesheet" href="https://fonts.googleapis.com/css2?family=M+PLUS+Rounded+1c:wght@400;700;800;900&display=swap">
<style>
  :root {
    --pink: #e8588f;
    --pink-soft: #f7c9da;
    --pink-pale: #fdeef3;
    --green: #7cbf3c;
    --green-dark: #5ea426;
    --ink: #555055;
    --grey: #8a8688;
    --line: #d9b6c4;
    --white: #ffffff;
  }
  * { margin: 0; padding: 0; box-sizing: border-box; }
  html, body { width: 849px; height: 1200px; overflow: hidden; }
  body {
    font-family: "M PLUS Rounded 1c", sans-serif;
    color: var(--ink);
    background: var(--white);
  }
  .flyer { position: relative; width: 849px; height: 1200px; overflow: hidden; background: var(--white); }

  .top-band { position: absolute; left: 0; top: 0; width: 849px; height: 420px;
    background: linear-gradient(180deg, var(--pink-pale) 0%, var(--white) 100%); }
  .bottom-band { position: absolute; left: 0; top: 788px; width: 849px; height: 412px; background: var(--pink-pale); }

  .clinic-title { position: absolute; left: 34px; top: 18px; font-size: 70px; line-height: 1.2; font-weight: 900;
    color: var(--pink); letter-spacing: 2px; white-space: nowrap; }
  .lead { position: absolute; left: 38px; top: 128px; font-size: 17px; color: var(--grey);
    padding-bottom: 4px; border-bottom: 3px solid var(--pink-soft); white-space: nowrap; }

  .open-date { position: absolute; left: 28px; top: 172px; color: var(--green); font-weight: 800;
    display: flex; align-items: baseline; }
  .open-date .num { font-size: 100px; line-height: 1; }
  .open-date .unit { font-size: 50px; margin: 0 6px 0 2px; }
  .weekday { display: inline-flex; align-items: center; justify-content: center; width: 54px; height: 54px;
    border-radius: 50%; background: var(--green); color: var(--white); font-size: 32px; line-height: 1; margin-left: 6px;
    align-self: center; }
  .open-word { position: absolute; left: 24px; top: 300px; font-size: 120px; font-weight: 900; line-height: 1;
    color: var(--green); letter-spacing: 4px; }

  .hero-art { position: absolute; left: 430px; top: 40px; width: 390px; height: 680px; border-radius: 45% 45% 20% 20%;
    background: radial-gradient(circle at 45% 25%, #fde3d0 0%, #f9d2e0 45%, #e8f3d6 100%); }
  .tagline { position: absolute; left: 690px; top: 450px; display: flex; flex-direction: column; align-items: center;
    background: var(--white); padding: 8px 6px; border-radius: 6px; transform: rotate(-22deg); transform-origin: top center; }
  .tagline span { display: block; font-size: 22px; line-height: 1.15; font-weight: 700; color: var(--green-dark); }

  .greeting { position: absolute; left: 30px; top: 530px; width: 390px; height: 195px; }
  .greeting-art { position: absolute; left: 0; top: 0; width: 70px; height: 80px; border-radius: 50% 50% 30% 30%;
    background: linear-gradient(180deg, #fbe0cc, #e3eef6); }
  .greeting-label { position: absolute; left: 82px; top: 10px; font-size: 17px; font-weight: 700; color: var(--ink); white-space: nowrap; }
  .greeting-lines { position: absolute; left: 82px; top: 40px; width: 308px; }
  .greeting-lines span { display: block; height: 26px; border-bottom: 2px dotted var(--line); }

  .preview-banner { position: absolute; left: 30px; top: 742px; width: 460px; height: 40px; border-radius: 20px;
    background: var(--green); color: var(--white); font-size: 20px; font-weight: 700; display: flex; align-items: center;
    justify-content: center; white-space: nowrap; }
  .welcome-text { position: absolute; left: 612px; top: 748px; font-size: 13px; color: var(--grey); white-space: nowrap; z-index: 2; }
  .welcome-art { position: absolute; left: 735px; top: 730px; width: 85px; height: 120px; border-radius: 50% 50% 20% 20%;
    background: linear-gradient(180deg, #fbe0cc, #f7c9da); }

  .preview-title { position: absolute; left: 30px; top: 796px; font-size: 64px; line-height: 1.2; font-weight: 900; color: var(--pink);
    letter-spacing: 3px; white-space: nowrap; }
  .preview-when { position: absolute; left: 560px; top: 796px; width: 175px; color: var(--pink); }
  .when-label { display: inline-block; background: var(--pink); color: var(--white); font-size: 17px; font-weight: 700;
    padding: 2px 10px; border-radius: 4px; }
  .when-date { display: flex; align-items: center; font-size: 44px; line-height: 1.1; font-weight: 800; white-space: nowrap; margin-top: 2px; }
  .when-date .weekday { width: 34px; height: 34px; font-size: 20px; background: var(--pink); }
  .when-time { font-size: 20px; font-weight: 700; color: var(--grey); white-space: nowrap; }

  .hours { position: absolute; left: 30px; top: 900px; display: flex; }
  .hours-label { width: 36px; background: var(--pink); color: var(--white); font-size: 15px; font-weight: 700;
    writing-mode: vertical-rl; display: flex; align-items: center; justify-content: center; letter-spacing: 3px; }
  .hours table { border-collapse: collapse; font-size: 14px; text-align: center; background: var(--white); }
  .hours th, .hours td { border: 1px solid var(--line); width: 38px; height: 28px; }
  .hours th { background: var(--pink-pale); font-weight: 700; }
  .hours td.time { width: 86px; background: var(--green); color: var(--white); font-size: 11px; white-space: nowrap; }
  .hours td { color: var(--pink); }

  .clinic-info { position: absolute; left: 30px; top: 1000px; }
  .clinic-name { font-size: 46px; line-height: 1.2; font-weight: 900; color: var(--pink); letter-spacing: 2px; white-space: nowrap; }
  .address { font-size: 15px; color: var(--grey); margin-top: 4px; white-space: nowrap; }
  .phone { display: flex; align-items: center; margin-top: 8px; font-size: 46px; line-height: 1.1; font-weight: 800; color: var(--pink); white-space: nowrap; }
  .phone svg { width: 40px; height: 40px; margin-right: 8px; }

  .map { position: absolute; left: 495px; top: 900px; width: 325px; height: 200px; border-radius: 6px;
    background: linear-gradient(135deg, #eeeeee, #dedede); }
  .map-pin-label { position: absolute; left: 520px; top: 925px; background: var(--white); border: 2px solid var(--pink);
    color: var(--pink); font-size: 15px; font-weight: 700; padding: 3px 10px; border-radius: 4px; white-space: nowrap; }
</style>
</head>
<body>
<main class="flyer">
  <div class="top-band"></div>
  <div class="bottom-band"></div>

  <h1 class="clinic-title">さくらだ接骨院</h1>
  <p class="lead">桜ヶ丘市に新しく接骨院を開業いたします。</p>

  <div class="open-date">
    <span class="num">0</span><span class="unit">月</span><span class="num">0</span><span class="unit">日</span><span class="weekday">土</span>
  </div>
  <div class="open-word">OPEN</div>

  <div class="hero-art" role="img" aria-label="ストレッチをする女性のイラスト"></div>
  <p class="tagline" aria-label="毎日の暮らしを快適に">
    <span>毎</span><span>日</span><span>の</span><span>暮</span><span>ら</span><span>し</span><span>を</span><span>快</span><span>適</span><span>に</span>
  </p>

  <section class="greeting">
    <div class="greeting-art" role="img" aria-label="院長のイラスト"></div>
    <h2 class="greeting-label">院長よりごあいさつ</h2>
    <div class="greeting-lines"><span></span><span></span><span></span><span></span><span></span><span></span></div>
  </section>

  <div class="preview-banner">OPENに先がけて内覧会を開催します</div>
  <div class="welcome-art" role="img" aria-label="スタッフのイラスト"></div>
  <p class="welcome-text">お待ちしています</p>

  <h2 class="preview-title">内覧会開催</h2>
  <div class="preview-when">
    <span class="when-label">開催日時</span>
    <div class="when-date">0月0日<span class="weekday">土</span></div>
    <p class="when-time">0:00 〜 00:00</p>
  </div>

  <section class="hours">
    <div class="hours-label">受付時間</div>
    <table>
      <tr><th></th><th>月</th><th>火</th><th>水</th><th>木</th><th>金</th><th>土</th><th>日祝</th></tr>
      <tr><td class="time">0:00〜00:00</td><td>●</td><td>●</td><td>●</td><td>●</td><td>●</td><td>●</td><td>／</td></tr>
      <tr><td class="time">00:00〜00:00</td><td>●</td><td>●</td><td>●</td><td>●</td><td>●</td><td>／</td><td>／</td></tr>
    </table>
  </section>

  <section class="clinic-info">
    <p class="clinic-name">さくらだ接骨院</p>
    <p class="address">〒000-0000 東県桜ヶ丘市0-0-0</p>
    <p class="phone">
      <svg viewBox="0 0 24 24" aria-hidden="true"><path fill="#e8588f" d="M6.6 10.8a15.1 15.1 0 0 0 6.6 6.6l2.2-2.2a1 1 0 0 1 1-.25 11.4 11.4 0 0 0 3.6.57 1 1 0 0 1 1 1V20a1 1 0 0 1-1 1A17 17 0 0 1 3 4a1 1 0 0 1 1-1h3.5a1 1 0 0 1 1 1c0 1.25.2 2.45.57 3.57a1 1 0 0 1-.25 1z"/></svg>
      000-0000-0000
    </p>
  </section>

  <div class="map" role="img" aria-label="接骨院周辺の地図"></div>
  <div class="map-pin-label">さくらだ接骨院</div>
</main>
</body>
</html>
```